business card for KestrelLine Construction
need a tag line (here to meet your needs)?
business card for KestrelLine Construction -
Creative Brief
Simple
Lorcan Whitlaney
Foreman
New Jersey or servicing north jersey
info@Kestrel-Line.com
www.Kestrel-Line.com
fully licensed fully insured
logo. residential commercial. 24hr emergency service. specializing in: *roofs *chimneys *masonry *gutters
logo. pic of workvan with logo Notes:________________________________________________________________________________________

```html
<!DOCTYPE html>
<html lang="en">
<head>
<meta charset="utf-8">
<title>KestrelLine Construction — Business Card</title>
<link rel="stylesheet" href="https://fonts.googleapis.com/css2?family=Open+Sans:ital,wght@0,400;0,600;0,700;0,800;1,400;1,600;1,700&display=swap">
<style>
  :root {
    --page-bg: #e9e6e1;
    --card-bg: #ffffff;
    --brand-blue: #1f2f8f;
    --brand-orange: #f39a1c;
    --text-grey: #7a7a7a;
    --text-dark: #4a4a4a;
    --divider: #c9c9c9;
  }
  * { box-sizing: border-box; margin: 0; padding: 0; }
  html, body {
    width: 1200px; height: 780px; overflow: hidden;
    background: var(--page-bg);
    font-family: "Open Sans", Arial, sans-serif;
  }
  .canvas {
    width: 1200px; height: 780px;
    display: flex; align-items: center; justify-content: center;
  }
  .business-card {
    position: relative;
    width: 1080px; height: 620px;
    background: var(--card-bg);
    border-radius: 36px;
    overflow: hidden;
    box-shadow: 0 6px 24px rgba(0,0,0,0.12);
  }
  .edge-bands { position: absolute; inset: 0; width: 100%; height: 100%; }
  .edge-band { fill: var(--brand-blue); }
  .edge-stripe { fill: none; stroke: var(--brand-orange); stroke-width: 7; }

  .brand-block {
    position: absolute; top: 78px; left: 0; right: 0;
    display: flex; align-items: center; justify-content: center; gap: 16px;
  }
  .brand-square { width: 34px; height: 34px; background: var(--brand-orange); }
  .brand-name {
    font-weight: 800; font-size: 58px; letter-spacing: -1px;
    color: var(--brand-blue); line-height: 1;
  }
  .brand-tagline {
    position: absolute; top: 168px; left: 0; right: 0;
    text-align: center;
    font-style: italic; font-weight: 700; font-size: 25px;
    color: var(--text-grey);
    word-spacing: 2px;
  }
  .brand-tagline .gap { display: inline-block; width: 22px; }

  .contact-person {
    position: absolute; top: 262px; left: 150px; width: 380px;
    text-align: right;
  }
  .person-name { font-weight: 700; font-size: 34px; color: var(--brand-blue); }
  .person-role { font-size: 26px; color: var(--brand-orange); margin-top: 2px; }
  .service-area { font-size: 26px; color: var(--text-dark); margin-top: 26px; }

  .divider {
    position: absolute; top: 236px; left: 560px;
    width: 2px; height: 210px; background: var(--divider);
  }

  .contact-list {
    position: absolute; top: 240px; left: 585px;
    list-style: none;
  }
  .contact-list li {
    display: flex; align-items: center; gap: 14px;
    font-size: 26px; color: var(--text-dark);
    height: 48px;
  }
  .contact-icon { width: 24px; height: 24px; fill: var(--brand-blue); flex: none; }

  .specialties {
    position: absolute; bottom: 58px; left: 165px;
    font-style: italic; font-weight: 700; font-size: 27px;
    color: var(--brand-blue);
    word-spacing: 4px;
  }
  .specialties .sep { color: var(--brand-orange); margin: 0 6px; }
  .specialties .label { margin-right: 14px; }
</style>
</head>
<body>
<div class="canvas">
  <article class="business-card">
    <svg class="edge-bands" viewBox="0 0 1080 620" preserveAspectRatio="none" aria-hidden="true">
      <path class="edge-band" d="M0,0 L40,0 C95,200 90,460 150,620 L0,620 Z"/>
      <path class="edge-stripe" d="M54,0 C108,200 104,460 166,620"/>
      <path class="edge-band" d="M1080,620 L1040,620 C985,420 990,160 930,0 L1080,0 Z"/>
      <path class="edge-stripe" d="M1026,620 C972,420 976,160 914,0"/>
    </svg>

    <header class="brand-block">
      <span class="brand-square" aria-hidden="true"></span>
      <h1 class="brand-name">KestrelLine Construction</h1>
    </header>
    <p class="brand-tagline">Residential &amp; Commercial.<span class="gap"></span>24hr emergency service.</p>

    <section class="contact-person">
      <p class="person-name">Lorcan Whitlaney</p>
      <p class="person-role">Foreman</p>
      <p class="service-area">Servicing North Jersey</p>
    </section>

    <div class="divider" aria-hidden="true"></div>

    <ul class="contact-list">
      <li>
        <svg class="contact-icon" viewBox="0 0 24 24" aria-hidden="true"><path d="M6.6 10.8a15 15 0 0 0 6.6 6.6l2.2-2.2a1 1 0 0 1 1-.25 11.4 11.4 0 0 0 3.6.57 1 1 0 0 1 1 1V20a1 1 0 0 1-1 1A17 17 0 0 1 3 4a1 1 0 0 1 1-1h3.5a1 1 0 0 1 1 1c0 1.25.2 2.45.57 3.57a1 1 0 0 1-.25 1z"/></svg>
        (T)1-888-555-0142
      </li>
      <li>
        <svg class="contact-icon" viewBox="0 0 24 24" aria-hidden="true"><path d="M6.6 10.8a15 15 0 0 0 6.6 6.6l2.2-2.2a1 1 0 0 1 1-.25 11.4 11.4 0 0 0 3.6.57 1 1 0 0 1 1 1V20a1 1 0 0 1-1 1A17 17 0 0 1 3 4a1 1 0 0 1 1-1h3.5a1 1 0 0 1 1 1c0 1.25.2 2.45.57 3.57a1 1 0 0 1-.25 1z"/></svg>
        201-555-0186
      </li>
      <li>
        <svg class="contact-icon" viewBox="0 0 24 24" aria-hidden="true"><path d="M12 2a10 10 0 1 0 5 18.7l-1-1.7A8 8 0 1 1 20 12v1.5a1.5 1.5 0 0 1-3 0V12a5 5 0 1 0-1.5 3.5A3.5 3.5 0 0 0 22 13.5V12A10 10 0 0 0 12 2zm0 13a3 3 0 1 1 0-6 3 3 0 0 1 0 6z"/></svg>
        info@Kestrel-Line.com
      </li>
      <li>
        <svg class="contact-icon" viewBox="0 0 24 24" aria-hidden="true"><path d="M12 2a10 10 0 1 0 0 20 10 10 0 0 0 0-20zm6.9 6h-2.9a15 15 0 0 0-1.4-3.6A8 8 0 0 1 18.9 8zM12 4a13 13 0 0 1 1.9 4h-3.8A13 13 0 0 1 12 4zM4.3 14a8 8 0 0 1 0-4h3.4a16 16 0 0 0 0 4zm.8 2h2.9a15 15 0 0 0 1.4 3.6A8 8 0 0 1 5.1 16zM8 8H5.1a8 8 0 0 1 4.3-3.6A15 15 0 0 0 8 8zm4 12a13 13 0 0 1-1.9-4h3.8A13 13 0 0 1 12 20zm2.3-6H9.7a14 14 0 0 1 0-4h4.6a14 14 0 0 1 0 4zm.3 5.6a15 15 0 0 0 1.4-3.6h2.9a8 8 0 0 1-4.3 3.6zm1.7-5.6a16 16 0 0 0 0-4h3.4a8 8 0 0 1 0 4z"/></svg>
        www.Kestrel-Line.com
      </li>
    </ul>

    <p class="specialties">
      <span class="label">Specializing in :</span>roofs<span class="sep">/</span>chimneys<span class="sep">/</span>masonry<span class="sep">/</span>gutters
    </p>
  </article>
</div>
</body>
</html>
```